Seeking a new website design for electrical contracting company

Brevard & Tolk electrical contracting needs a new website for brevard-tolk.com

We are looking for modern and something real cool with motion for a landing page. we have some cool images from our photo shoot. maybe even 3d motion our existing logo. we would like something we can edit with news and events and update a past project page. Also allow to take payment
stock images at
https://miraelsworthimages.pixgallery.com/Brevard-and-Tolk

Target Market(s)

construction , home owners , business owners,

Industry/Entity Type

construction , electrical

Coding

Coded - Design and coding required

Number of Pages Required

5+ page

Font styles to use
Serif
Sans Serif

Colors
0054AA
0677BA
7BADD7
CADEEF
E8F1F8
0094D4
00A9DD
6FCCEA
C7EBF8
E9F6FB
FFF300
FFF600
FEFA6F
FFFEC7
FFFEE8

Requirements
Must have
• excitement, motion, selling professionalism,

```html
<!DOCTYPE html>
<html lang="en">
<head>
<meta charset="utf-8">
<title>Brevard &amp; Tolk Electrical Contracting</title>
<link rel="stylesheet" href="https://fonts.googleapis.com/css2?family=Lato:ital,wght@0,400;0,700;0,900;1,700&family=Roboto:wght@400&display=swap">
<style>
:root{
  --blue-deep:#0054AA;
  --blue:#0677BA;
  --blue-bright:#0094D4;
  --blue-pale:#E8F1F8;
  --blue-soft:#CADEEF;
  --yellow:#FFF300;
  --yellow-soft:#FEFA6F;
  --ink:#1a1f2e;
  --white:#fff;
}
*{box-sizing:border-box;margin:0;padding:0}
html,body{width:1200px;height:3158px;overflow:hidden}
body{position:relative;background:var(--white);font-family:"Lato",sans-serif;color:var(--ink)}
.abs{position:absolute}
a{color:inherit;text-decoration:none}

/* header */
.site-header{position:absolute;left:0;top:0;width:1200px;height:85px;background:var(--white);z-index:3}
.brand{position:absolute;display:flex;align-items:center;gap:10px;color:var(--blue-deep);font-weight:900;font-size:26px;letter-spacing:.3px;white-space:nowrap}
.brand-dot{width:40px;height:40px;border-radius:50%;background:var(--blue-deep)}
.site-header .brand{left:78px;top:22px}
.main-nav{position:absolute;left:427px;top:32px;display:flex;gap:23px;font-size:15px;color:#333}
.main-nav .active{color:var(--blue-deep)}
.btn{position:absolute;display:flex;align-items:center;justify-content:center;background:var(--yellow);color:var(--blue-deep);font-weight:700;font-size:19px;border:1px solid #d9cf00}
.site-header .btn{left:919px;top:20px;width:169px;height:46px}

/* hero */
.hero{position:absolute;left:0;top:85px;width:1200px;height:530px}
.hero-title{position:absolute;left:0;top:80px;width:1200px;text-align:center;color:var(--white);font-weight:700;font-size:51px;line-height:60px;text-shadow:0 2px 6px rgba(0,0,0,.5)}
.hero .btn{left:506px;top:213px;width:168px;height:45px}

/* about */
.about-title{left:642px;top:680px;font-size:40px;font-weight:700;color:var(--blue-deep)}
.about-title span,.light-bg .section-title span{color:var(--blue-bright)}
.about-list{left:642px;top:746px;width:440px;list-style:none;font-size:14.5px;line-height:28.2px;color:#333}
.about-list li{position:relative;padding-left:25px;padding-right:14px}
.about-list svg{position:absolute;left:0;top:7px}
.about .btn{left:642px;top:968px;width:170px;height:47px}

/* projects */
.projects{position:absolute;left:0;top:1122px;width:1200px;height:556px;background:var(--blue-deep);color:var(--white)}
.section-title{position:absolute;left:0;width:1200px;text-align:center;font-weight:700;font-size:42px}
.projects .section-title{top:74px}
.project{position:absolute;top:156px;width:396px}
.project h3{font-size:35px;font-weight:700;margin-top:18px;margin-bottom:10px}
.project p{font-size:15px;line-height:27.6px;padding-left:2px;height:138px;overflow:hidden}
.read-more{font-style:italic;font-weight:700;font-size:19px;display:block;margin-top:10px}
.divider{position:absolute;left:598px;top:170px;width:4px;height:300px;background:var(--yellow);border-radius:2px}

/* services */
.services .section-title{top:1756px;color:var(--blue-deep)}
.service{position:absolute;top:1825px;width:309px}
.service .photo{width:309px;height:293px;border-radius:8px;box-shadow:0 3px 8px rgba(0,0,0,.18)}
.service h4{text-align:center;font-size:22px;font-weight:700;margin-top:28px;color:#111}
.arrow{position:absolute}

/* behind the scenes */
.scenes{position:absolute;left:0;top:2245px;width:1200px;height:600px;background:var(--blue-pale)}
.scenes .section-title{top:72px;color:var(--blue-deep)}
.post{position:absolute;top:135px;width:309px;height:300px;background:var(--white);box-shadow:0 2px 8px rgba(0,0,0,.12)}
.post .photo{height:152px}
.post-body{padding:14px 16px}
.post h5{font-size:15px;font-weight:700;color:#111}
.meta{display:flex;justify-content:space-between;font-size:12.5px;color:#444;margin-top:7px;padding-right:14px}
.post p{font-size:12.5px;line-height:22px;margin-top:7px;height:44px;overflow:hidden}
.post .read-more{font-size:16px;margin-top:3px}

/* footer */
.footer-col h6{font-size:19px;font-weight:400;color:var(--blue-deep);font-family:"Lato",sans-serif}
.quick-links{left:223px;top:2880px}
.quick-links ul{list-style:none;margin-top:8px;font-size:15px;line-height:28.2px}
.quick-links li::before{content:"";display:inline-block;width:8px;height:8px;background:var(--blue-deep);margin-right:12px;vertical-align:2px}
.site-footer .brand{left:464px;top:2885px}
.socials{left:502px;top:2982px;display:flex;gap:14px}
.socials span{width:29px;height:29px;border-radius:50%;background:var(--blue-deep);display:block}
.contact{left:836px;top:2880px}
.contact-item{display:flex;gap:8px;align-items:flex-start;font-family:"Roboto",sans-serif;font-size:15px;line-height:27px;margin-top:10px}
.rule{left:110px;top:3103px;width:980px;height:1px;background:#bbb}
.copyright{left:0;top:3120px;width:1200px;text-align:center;font-size:15px}
</style>
</head>
<body>

<header class="site-header">
  <a class="brand" href="#"><span class="brand-dot"></span>Brevard &amp; Tolk</a>
  <nav class="main-nav">
    <a class="active" href="#">Home</a><a href="#">About</a><a href="#">Services</a><a href="#">Project</a><a href="#">Testimonials</a><a href="#">Blog</a>
  </nav>
  <a class="btn" href="#">Contact Us</a>
</header>

<section class="hero">
  <svg class="abs" style="left:0;top:0" width="1200" height="530" viewBox="0 0 1200 530">
    <defs>
      <linearGradient id="heroFill" x1="0" y1="0" x2="1" y2="1">
        <stop offset="0" stop-color="#4a5566"/>
        <stop offset=".45" stop-color="#2f3540"/>
        <stop offset=".8" stop-color="#5a4a44"/>
        <stop offset="1" stop-color="#a9adb2"/>
      </linearGradient>
    </defs>
    <polygon role="img" aria-label="Crew of five electricians standing in front of company vans and trucks by a brick building" points="0,0 1200,0 1200,455 600,520 0,455" fill="url(#heroFill)"/>
    <polygon points="0,455 600,520 1200,455 1200,460 600,525 0,472" fill="var(--blue-deep)"/>
  </svg>
  <h1 class="hero-title">Powering Every Project.<br>Wired for Life.</h1>
  <a class="btn" href="#">Contact Us</a>
</section>

<section class="about">
  <svg class="abs" style="left:107px;top:610px" width="458" height="484" viewBox="0 0 458 484">
    <defs>
      <linearGradient id="aboutFill" x1="0" y1="0" x2="0" y2="1">
        <stop offset="0" stop-color="#7a4436"/>
        <stop offset=".5" stop-color="#3b3f4a"/>
        <stop offset="1" stop-color="#2c2f36"/>
      </linearGradient>
    </defs>
    <polygon points="226,2 456,125 456,354 232,482 2,356 2,126" fill="none" stroke="var(--blue-bright)" stroke-width="2"/>
    <polygon role="img" aria-label="Five electricians posing in front of a company van" points="226,18 442,140 442,342 232,465 16,342 16,140" fill="url(#aboutFill)"/>
  </svg>
  <h2 class="about-title abs">About <span>Us</span></h2>
  <ul class="about-list abs">
    <li><svg width="16" height="16" viewBox="0 0 16 16"><circle cx="8" cy="8" r="7" fill="none" stroke="#333" stroke-width="1.2"/><path d="M4.5 8h6M8.5 5.5 11 8l-2.5 2.5" fill="none" stroke="#333" stroke-width="1.2"/></svg>We’re a licensed team of electricians serving homes and businesses. From the first walkthrough to the final inspection, we deliver safe, code-compliant work that powers, protects, and lasts for years.</li>
    <li><svg width="16" height="16" viewBox="0 0 16 16"><circle cx="8" cy="8" r="7" fill="none" stroke="#333" stroke-width="1.2"/><path d="M4.5 8h6M8.5 5.5 11 8l-2.5 2.5" fill="none" stroke="#333" stroke-width="1.2"/></svg>Whether it’s a new panel, a full commercial build-out, or a repair that stumped others — we keep the lights on. Literally.</li>
  </ul>
  <a class="btn" href="#">Contact Us</a>
</section>

<section class="projects">
  <h2 class="section-title">Our Project</h2>
  <article class="project" style="left:108px">
    <svg width="82" height="80" viewBox="0 0 82 80" fill="none" stroke="#fff" stroke-width="2.5">
      <rect x="3" y="3" width="76" height="56" rx="3"/><path d="M3 50h76M34 59v10M48 59v10M24 74h34"/>
      <path d="M8 30h12l5-10 6 18 5-12h10l5-8 6 14h16"/><ellipse cx="41" cy="28" rx="14" ry="9"/><circle cx="41" cy="28" r="4"/>
    </svg>
    <h3>Brightline Studios</h3>
    <p>We partnered with Brightline to power their new studio with a complete electrical build-out. Centered on safety and uptime, the job featured a 400-amp service upgrade, LED lighting throughout, and dedicated circuits for their production gear. Built to run for decades.</p>
    <a class="read-more" href="#">Read More..</a>
  </article>
  <div class="divider"></div>
  <article class="project" style="left:692px">
    <svg width="82" height="80" viewBox="0 0 82 80" fill="none" stroke="#fff" stroke-width="2.5">
      <rect x="3" y="3" width="14" height="14"/><path d="M6 10l3 3 5-6"/><rect x="63" y="18" width="14" height="14"/><path d="M66 25l3 3 5-6"/>
      <rect x="3" y="46" width="14" height="14"/><path d="M6 53l3 3 5-6"/><rect x="63" y="62" width="14" height="14"/><path d="M66 69l3 3 5-6"/>
      <circle cx="41" cy="40" r="10"/><circle cx="41" cy="40" r="4"/><path d="M17 10h26v10M63 25H52M17 53h14M52 48h8v14M28 68h26M28 68l5-4M28 68l5 4"/>
    </svg>
    <h3>Studio Halden</h3>
    <p>For Halden Works’s renovation, we planned a sleek, efficient lighting and power layout that lets them reconfigure their office with ease. The job included smart switching, floor outlets, EV chargers, and subtle fixtures that bring the space to life.</p>
    <a class="read-more" href="#">Read More..</a>
  </article>
</section>

<section class="services light-bg">
  <h2 class="section-title">Our <span>Services</span></h2>
  <svg class="arrow" style="left:46px;top:1968px" width="16" height="24" viewBox="0 0 16 24"><path d="M12 3 4 12l8 9" fill="none" stroke="#444" stroke-width="2.5"/></svg>
  <svg class="arrow" style="left:1134px;top:1968px" width="16" height="24" viewBox="0 0 16 24"><path d="M4 3l8 9-8 9" fill="none" stroke="#444" stroke-width="2.5"/></svg>
  <div class="service" style="left:110px">
    <div class="photo" role="img" aria-label="Electrician in hard hat testing a wall panel" style="background:linear-gradient(135deg,#3d5a78,#d9772a 55%,#2b3b52)"></div>
    <h4>Residential Electrical</h4>
  </div>
  <div class="service" style="left:451px">
    <div class="photo" role="img" aria-label="Electrician on a ladder installing ceiling lights in a commercial space" style="background:linear-gradient(180deg,#5a6f80,#8ea4b4 55%,#c8cfd4)"></div>
    <h4>Commercial Electrical</h4>
  </div>
  <div class="service" style="left:779px">
    <div class="photo" role="img" aria-label="Electrician wiring an electrical panel" style="background:linear-gradient(135deg,#2a3444,#5b6a7c 50%,#c98a3a)"></div>
    <h4>Electrical Panel Upgrades</h4>
  </div>
</section>

<section class="scenes light-bg">
  <h2 class="section-title">Behind the <span>Scenes</span></h2>
  <svg class="arrow" style="left:46px;top:268px" width="16" height="24" viewBox="0 0 16 24"><path d="M12 3 4 12l8 9" fill="none" stroke="#444" stroke-width="2.5"/></svg>
  <svg class="arrow" style="left:1134px;top:268px" width="16" height="24" viewBox="0 0 16 24"><path d="M4 3l8 9-8 9" fill="none" stroke="#444" stroke-width="2.5"/></svg>
  <article class="post" style="left:112px">
    <div class="photo" role="img" aria-label="Hands stripping wires with pliers" style="background:linear-gradient(180deg,#e4e6ea,#b9bcc2 60%,#d6a88a)"></div>
    <div class="post-body">
      <h5>Your Breakers Trip Frequently</h5>
      <div class="meta"><span>April 5, 2025</span><span>Safety Tips</span></div>
      <p>Why breakers keep tripping, and when it is time to call a licensed electrician.</p>
      <a class="read-more" href="#">Read more..</a>
    </div>
  </article>
  <article class="post" style="left:446px">
    <div class="photo" role="img" aria-label="Hand installing a wall outlet" style="background:linear-gradient(90deg,#8c8c8c,#dcdcdc 50%,#c9c2b8)"></div>
    <div class="post-body">
      <h5>Lights Flicker or Dim Unexpectedly</h5>
      <div class="meta"><span>March 2, 2025</span><span>Troubleshooting</span></div>
      <p>Common causes of flicker, from loose connections to overloaded circuits.</p>
      <a class="read-more" href="#">Read more..</a>
    </div>
  </article>
  <article class="post" style="left:780px">
    <div class="photo" role="img" aria-label="Hand holding a damaged power plug" style="background:linear-gradient(90deg,#3f5a6a,#9fb0b8 55%,#d9d9d9)"></div>
    <div class="post-body">
      <h5>Burning Smells or Warm Outlets</h5>
      <div class="meta"><span>January 28, 2025</span><span>Home Safety</span></div>
      <p>Heat or burning smells at an outlet are warnings you should never ignore.</p>
      <a class="read-more" href="#">Read more..</a>
    </div>
  </article>
</section>

<footer class="site-footer">
  <svg class="abs" style="left:0;top:2760px" width="1200" height="80" viewBox="0 0 1200 80">
    <polygon points="0,0 1200,0 1200,72 600,8 0,72" fill="var(--blue-pale)"/>
    <polyline points="0,76 600,10 1200,76" fill="none" stroke="var(--blue-deep)" stroke-width="7"/>
  </svg>
  <div class="footer-col quick-links abs">
    <h6>Quick Links</h6>
    <ul><li>Home</li><li>About</li><li>Project</li><li>Services</li><li>Blog</li></ul>
  </div>
  <a class="brand" href="#"><span class="brand-dot"></span>Brevard &amp; Tolk</a>
  <div class="socials abs"><span></span><span></span><span></span><span></span></div>
  <div class="footer-col contact abs">
    <h6>Contact Us</h6>
    <div class="contact-item"><svg width="28" height="28" viewBox="0 0 28 28"><circle cx="14" cy="14" r="14" fill="var(--blue-deep)"/><path d="M10 7l3 4-2 2c1 2 3 4 5 5l2-2 4 3-2 3c-6 0-13-7-13-13z" fill="#fff"/></svg><span>888 888 88</span></div>
    <div class="contact-item"><svg width="28" height="28" viewBox="0 0 28 28"><circle cx="14" cy="14" r="14" fill="var(--blue-deep)"/><rect x="7" y="9" width="14" height="10" fill="none" stroke="#fff" stroke-width="1.6"/><path d="M7 9l7 6 7-6" fill="none" stroke="#fff" stroke-width="1.6"/></svg><span>info@brevard-tolk.com</span></div>
    <div class="contact-item"><svg width="28" height="28" viewBox="0 0 28 28"><circle cx="14" cy="14" r="14" fill="var(--blue-deep)"/><path d="M14 6a5 5 0 0 1 5 5c0 4-5 10-5 10s-5-6-5-10a5 5 0 0 1 5-5z" fill="#fff"/><circle cx="14" cy="11" r="2" fill="var(--blue-deep)"/></svg><span>BREVARD &amp; TOLK<br>ELECTRICAL CONTRACTORS<br>Dale Brevard 1-555-234-8871</span></div>
  </div>
  <div class="rule abs"></div>
  <p class="copyright abs">Copyright © 2025. Brevard &amp; Tolk electrical contracting. All Rights Reserved</p>
</footer>

</body>
</html>
```